Harbor Ridge Holdings, LLC Business Card Design/Real Estate and Asset Mgmt.

Design business card with designer recommended colors using existing logo...teal color not mandatory. Business purpose is Asset Management and Real Estate.

The following text somewhere on the card:

HARBOR RIDGE HOLDINGS, LLC (llc can be very small font if needed.)
Tobias Welk GRI, RRP, CHA, CHME (the abbreviations can be a smaller font)
PROPLICENSEE
517 Fenwick Lane #204-31
Lakemont, TN 38999
Toll Free: 888-555-0172
Cell: 931.555.0148
Email: tobiasrwelk@mailpost.example
www.harborridgeholdings.example

Target Market(s)

High net worth buyers and sellers. Will be providing commercial real estate sales and management services to banks and lenders who foreclose on bad debt collateral.

Industry/Entity Type

Real Estate

Contact Information for Business Card

Professional look. Maximum of two colors. Example: Logo one color and the text another. Or any combination the designer feels is appropriate.

Font styles to use
Other font styles liked:
• Designer's choice

Requirements
Must have
• Logo somewhere on the card.
Nice to have
• The card can be one sided or two sided or odd sized if the designer prefers.
• PROPLICENSEE Logo (small at the bottom or somewhere on the card. Even the back.)
Should not have
• Card should not be a folded card.

```html
<!DOCTYPE html>
<html lang="en">
<head>
<meta charset="utf-8">
<title>Harbor Ridge Holdings, LLC — Business Card</title>
<link rel="stylesheet" href="https://fonts.googleapis.com/css2?family=Tinos:wght@400;700&family=Cormorant+Garamond:wght@400;500&display=swap">
<style>
  :root {
    --teal: #2593a0;
    --ink: #1d1d1d;
    --ink-soft: #3a3a3a;
    --paper: #f7f7f6;
    --stage: #eceded;
    --white: #ffffff;
  }
  * { margin: 0; padding: 0; box-sizing: border-box; }
  html, body { width: 1200px; height: 698px; overflow: hidden; }
  body {
    background: var(--stage);
    font-family: "Tinos", "Times New Roman", serif;
    position: relative;
  }
  .card {
    position: absolute;
    top: 200px;
    width: 520px;
    height: 297px;
    box-shadow: 0 6px 18px rgba(0,0,0,0.10), 0 1px 3px rgba(0,0,0,0.08);
  }
  /* Front */
  .card-front { left: 70px; background: var(--paper); }
  .accent-square {
    position: absolute; left: 0; top: 96px;
    width: 14px; height: 14px; background: var(--teal);
  }
  .agent {
    position: absolute; right: 34px; top: 56px; text-align: right;
  }
  .agent-name {
    font-weight: 700; font-size: 23px; letter-spacing: 1px;
    color: var(--teal); text-transform: uppercase; white-space: nowrap;
  }
  .agent-creds {
    font-size: 12px; font-weight: 400; letter-spacing: 0.5px; margin-left: 4px;
  }
  .agent-title {
    margin-top: 6px; font-size: 11px; font-weight: 700;
    letter-spacing: 0.8px; color: var(--ink);
  }
  .company-block { position: absolute; left: 30px; top: 112px; }
  .company-name {
    font-weight: 700; font-size: 15px; letter-spacing: 0.6px;
    color: var(--ink); text-transform: uppercase; margin-bottom: 10px;
  }
  .contact-line {
    display: flex; align-items: center; gap: 6px; white-space: nowrap;
    font-size: 11.5px; color: var(--ink-soft); line-height: 1; margin-bottom: 8px;
  }
  .contact-line svg { width: 10px; height: 10px; flex: none; }
  .divider { color: var(--teal); margin: 0 3px; }
  /* Back */
  .card-back {
    left: 610px; background: var(--teal);
    display: flex; flex-direction: column; align-items: center; justify-content: center;
    color: var(--white);
  }
  .brand {
    display: flex; align-items: center; gap: 12px; white-space: nowrap;
    font-family: "Cormorant Garamond", "Times New Roman", serif;
    font-weight: 500; font-size: 27px; letter-spacing: 1.5px; text-transform: uppercase;
  }
  .brand-mark { width: 16px; height: 16px; background: var(--white); }
  .brand-llc { font-size: 14px; letter-spacing: 1px; }
  .brand-url {
    margin-top: 10px;
    font-family: "Cormorant Garamond", "Times New Roman", serif;
    font-size: 16px; letter-spacing: 0.5px;
  }
</style>
</head>
<body>
  <section class="card card-front" aria-label="Business card front">
    <span class="accent-square"></span>
    <div class="agent">
      <div class="agent-name">Tobias Welk<span class="agent-creds">GRI, RRP, CHA, CHME</span></div>
      <div class="agent-title">PROPLICENSEE</div>
    </div>
    <div class="company-block">
      <div class="company-name">Harbor Ridge Holdings LLC</div>
      <div class="contact-line">
        <svg viewBox="0 0 10 10" aria-hidden="true"><path d="M5 0.5a3.3 3.3 0 0 0-3.3 3.3C1.7 6.3 5 9.5 5 9.5s3.3-3.2 3.3-5.7A3.3 3.3 0 0 0 5 0.5z" fill="var(--teal)"/><circle cx="5" cy="3.8" r="1.2" fill="var(--paper)"/></svg>
        517 Fenwick Lane #204-31 Lakemont, TN 38999
      </div>
      <div class="contact-line">
        <svg viewBox="0 0 10 10" aria-hidden="true"><rect x="2.5" y="0.5" width="5" height="9" rx="1" fill="var(--teal)"/><rect x="3.3" y="1.6" width="3.4" height="5.8" fill="var(--paper)"/></svg>
        931.555.0148<span class="divider">|</span>
        <svg viewBox="0 0 10 10" aria-hidden="true"><path d="M2 1l2 0 1 2.3-1.2 1a5.5 5.5 0 0 0 2.4 2.4l1-1.2L9.5 6.5v2c0 .5-.5 1-1 1A8.5 8.5 0 0 1 1 2c0-.5.5-1 1-1z" fill="var(--teal)"/></svg>
        888-555-0172
      </div>
      <div class="contact-line">
        <svg viewBox="0 0 10 10" aria-hidden="true"><rect x="0.5" y="2" width="9" height="6.5" fill="none" stroke="var(--teal)" stroke-width="1"/><path d="M0.5 2l4.5 3.6L9.5 2" fill="none" stroke="var(--teal)" stroke-width="1"/></svg>
        tobiasrwelk@mailpost.example<span class="divider">|</span>
        <svg viewBox="0 0 10 10" aria-hidden="true"><circle cx="5" cy="5" r="4.3" fill="none" stroke="var(--teal)" stroke-width="1"/><path d="M0.7 5h8.6M5 0.7c-2.4 2.6-2.4 6 0 8.6M5 0.7c2.4 2.6 2.4 6 0 8.6" fill="none" stroke="var(--teal)" stroke-width="0.8"/></svg>
        www.harborridgeholdings.example
      </div>
    </div>
  </section>

  <section class="card card-back" aria-label="Business card back">
    <div class="brand">
      <span class="brand-mark"></span>
      <span>Harbor Ridge Holdings, <span class="brand-llc">LLC</span></span>
    </div>
    <div class="brand-url">harborridgeholdings.example</div>
  </section>
</body>
</html>
```